Flyer Mail out

Need something urgently designed.

I need a flyer done double sided I have provided CWDG photos and the writing. I do not have any dental surgery stock photos as such but this can be used. We are a mobile dental company that goes out to schools and provide free dental services.

I have attached the written document and would like it double sided A4 paper.

The colours I want is Aqua, Light Blue, dark blue, grey and white.

Just need it designed beautifully and professionally to go out to principals to contact us and use our services.

If you would like more info have a look at our Chatterloop page Coastline Wandering Dental Group

```html
<!DOCTYPE html>
<html lang="en">
<head>
<meta charset="utf-8">
<title>Coastline Wandering Dental Group – School Flyer</title>
<link href="https://fonts.googleapis.com/css2?family=Fira+Sans:ital,wght@0,400;0,500;0,600;1,400;1,500&display=swap" rel="stylesheet">
<style>
  :root {
    --backdrop: #e9e8e9;
    --paper: #ffffff;
    --aqua: #1ba6de;
    --aqua-light: #9fd6ee;
    --navy: #1b4e8a;
    --navy-deep: #124a80;
    --grey: #d3d4d6;
    --grey-light: #efeff0;
    --ink: #3a3a3a;
  }
  * { box-sizing: border-box; margin: 0; padding: 0; }
  html, body { width: 1200px; height: 1000px; overflow: hidden; background: var(--backdrop); }
  body { font-family: "Fira Sans", Arial, sans-serif; position: relative; }

  .flyer {
    position: absolute; left: 270px; top: 28px;
    width: 660px; height: 945px; background: var(--paper);
    box-shadow: 0 18px 40px rgba(0,0,0,0.18);
    overflow: hidden;
  }

  .hero-photo {
    position: absolute; left: 0; top: 0; width: 660px; height: 444px;
    background: linear-gradient(180deg, #c9d6e0 0%, #e8ecef 30%, #9aa3aa 60%, #3d4247 100%);
  }
  .hero-band {
    position: absolute; left: 0; top: 394px; width: 660px; height: 50px;
    background: linear-gradient(90deg, rgba(27,166,222,0.25), rgba(27,166,222,0.55) 50%, rgba(27,166,222,0.25));
  }
  .hero-quote {
    position: absolute; left: 0; top: 402px; width: 660px;
    text-align: center; color: #fff; font-size: 25px; font-weight: 500; letter-spacing: 0.3px;
  }

  .stat-band {
    position: absolute; left: 0; top: 444px; width: 660px; height: 124px;
    background: var(--aqua); color: #fff; padding: 18px 38px 0;
  }
  .stat-band .stat { font-style: italic; font-size: 17.5px; line-height: 1.35; }
  .stat-band .stat small { font-size: 12.5px; }
  .stat-band .note { font-style: italic; font-size: 12.5px; line-height: 1.55; }

  .booking {
    position: absolute; left: 0; top: 568px; width: 437px; height: 170px;
    background: var(--grey-light);
    display: flex; align-items: center; justify-content: center; text-align: center;
  }
  .booking h2 { color: var(--navy); font-size: 27px; font-weight: 500; line-height: 1.3; }

  .reference {
    position: absolute; left: 437px; top: 568px; width: 223px; height: 34px;
    background: var(--navy-deep); color: #fff; font-size: 9px; font-style: italic;
    padding: 10px 0 0 6px;
  }
  .clinic-photo {
    position: absolute; left: 437px; top: 602px; width: 223px; height: 343px;
    background: linear-gradient(160deg, #f4f6f7 0%, #dfe8ee 45%, #7f8a93 80%, #5b636b 100%);
  }

  .contact {
    position: absolute; left: 0; top: 738px; width: 437px; height: 190px;
    background: var(--grey); padding: 42px 22px 0 36px;
    color: var(--ink); font-size: 10.5px; line-height: 1.75;
  }
  .contact li { list-style: none; }
  .contact li::before { content: "• "; }
  .contact .link { color: var(--navy); font-style: italic; font-weight: 500; }

  .brand {
    position: absolute; left: 36px; top: 905px; height: 22px;
    display: flex; align-items: center; gap: 5px;
    background: #fff; padding: 0 6px;
    color: var(--navy-deep); font-size: 7.5px;
  }
  .brand .mark { width: 9px; height: 9px; background: var(--navy-deep); }

  .foot-strip {
    position: absolute; left: 0; top: 928px; width: 437px; height: 17px;
    background: var(--aqua-light);
  }
</style>
</head>
<body>
  <main class="flyer">
    <div class="hero-photo" role="img" aria-label="Photo of the dental team in uniforms standing in front of the white mobile dental truck"></div>
    <div class="hero-band"></div>
    <p class="hero-quote">“OUR FOCUS IS ON EDUCATION &amp; PREVENTION”</p>

    <section class="stat-band">
      <p class="stat">“1 in 5 children between the ages of 4-8 years of age will suffer from tooth decay or dental caries as a result of poor dental hygiene”* <small>- Thus, leading to possible dental</small></p>
      <p class="note">destruction to their adult teeth. This, in conjunction with diet, lifestyle and social welfare can be contribution to the increase of child absenteeism.</p>
    </section>

    <section class="booking">
      <h2>Book us now for 2015 and help<br>us, bring back your student’s<br>“bright smile”</h2>
    </section>

    <p class="reference">*ref. The Southern Child Health Council</p>
    <div class="clinic-photo" role="img" aria-label="Photo of two smiling dental staff members in the treatment room of the mobile clinic"></div>

    <ul class="contact">
      <li>To find out about our procedures or to book your school for <em>2015</em> and take advantage of this opportunity, Please visit our website <span class="link">www.cwdg.net.au</span> or email me at <span class="link">Mara.k@cwdg.net.au</span>.</li>
      <li>To speak to one of our friendly staff, call us directly on <span class="link">(02) 5550 1427</span>.</li>
      <li>In addition, feel free to visit <span class="link">Chatterloop/Chirpline/Linkroster</span> to see regular updates, features, special offers and daily tips regarding our services.</li>
    </ul>

    <div class="brand"><span class="mark"></span>Coastline Wandering Dental Group</div>
    <div class="foot-strip"></div>
  </main>
</body>
</html>
```